Cell Tower company needs website updated

We need a website that does not look like it was designed in the early 1990's. The company fabricates, installs and reinforces communication towers throughout the US, Caribbean, Central and S. America. We are located in Pensacola Florida. Our tower technicians travel to wherever the work is. I have some good pictures taken from towers to use on the site. I want the site to reflect the excitement that the wireless communication industry has. I want to the company to look exciting and attract new employees. The majority of our business is modifying and reinforcing existing cell towers to accept all the new tower top antennas that the increasing wireless mobile world demands.
Updates

I have added some sample photos from our business to our ArtBazaar profile.

We are now going through each design to find what is most suitable for our needs. Thank you all for your time in this matter.

Industry/Entity Type

Wireless Communication

```html
<!DOCTYPE html>
<html lang="en">
<head>
<meta charset="utf-8">
<title>TowerLine — Towering Above the Rest</title>
<link href="https://fonts.googleapis.com/css2?family=Roboto:wght@300;400;500;700&display=swap" rel="stylesheet">
<style>
:root{
  --red:#e0201e;
  --ink:#333;
  --muted:#888;
  --faint:#b5b5b5;
  --line:#e3e3e3;
  --paper:#fff;
  --section:#f7f7f7;
  --footer:#333;
  --footer-deep:#2a2a2a;
  --footer-text:#aaa;
}
*{margin:0;padding:0;box-sizing:border-box}
html,body{width:913px;height:1200px;overflow:hidden}
body{font-family:'Roboto',sans-serif;background:var(--paper);color:var(--ink);position:relative}

/* header */
.site-header{position:absolute;left:0;top:0;width:913px;height:90px;background:var(--paper)}
.brand{position:absolute;left:44px;top:36px;display:flex;align-items:center;gap:6px;font-size:25px;font-weight:400;color:var(--ink);letter-spacing:-.3px}
.brand-dot{width:10px;height:10px;background:var(--red);border-radius:50%}
.topbar{position:absolute;left:256px;top:0;width:611px;height:35px;border-bottom:1px solid var(--line);font-size:10px}
.jobs{position:absolute;left:0;top:11px;color:var(--muted)}
.jobs b{color:#555;font-weight:500}
.call{position:absolute;right:170px;top:11px;color:var(--red);font-weight:700;letter-spacing:.5px;display:flex;align-items:center;gap:4px}
.search{position:absolute;right:0;top:0;width:147px;height:35px;border-left:1px solid var(--line);color:var(--faint);padding:11px 0 0 11px}
.search svg{position:absolute;right:6px;top:10px}
.main-nav{position:absolute;left:264px;top:57px;display:flex;font-size:10px;color:#666}
.main-nav span{margin-right:28px}
.main-nav .caret{font-size:8px;margin-left:2px}

/* hero */
.hero{position:absolute;left:0;top:90px;width:913px;height:361px;
  background:linear-gradient(100deg,#1b1e26 0%,#3a3b40 22%,#5a5046 40%,#8d7452 55%,#6a5c47 75%,#3e3d3a 100%)}
.hero::after{content:"";position:absolute;left:0;top:0;right:0;bottom:0;
  background:radial-gradient(ellipse 260px 120px at 560px 110px,rgba(255,220,150,.55),transparent),linear-gradient(180deg,transparent 55%,rgba(20,22,20,.6))}
.hero-copy{position:absolute;left:0;width:913px;top:128px;text-align:center;color:#fff;z-index:1}
.hero-title{font-size:45px;font-weight:400;letter-spacing:1px;line-height:1}
.hero-title em{font-style:normal;color:var(--red)}
.hero-sub{font-size:22px;font-weight:400;letter-spacing:1.5px;margin-top:15px}
.btn{display:inline-block;background:var(--red);color:#fff;font-weight:500;letter-spacing:.8px;border-radius:2px}
.hero .btn{margin-top:24px;font-size:10px;padding:11px 12px}

/* overview */
.overview{position:absolute;left:0;top:451px;width:913px;height:525px;background:var(--section);text-align:center}
.eyebrow{position:absolute;left:0;width:913px;top:57px;font-size:10px;font-weight:500;letter-spacing:1px;color:#444}
.rule{position:absolute;left:428px;top:96px;width:57px;height:1px;background:var(--line)}
.lead{position:absolute;left:0;width:913px;top:113px;font-size:21px;font-weight:300;line-height:30px;color:#666}
.overview .btn-about{position:absolute;left:392px;top:186px;width:130px;height:27px;line-height:27px;font-size:9px;padding:0}
.services-title{position:absolute;left:0;width:913px;top:261px;font-size:23px;font-weight:300;color:var(--red)}
.service{position:absolute;top:320px;width:282px;text-align:center}
.service-art{width:34px;height:64px;margin:0 auto;background:linear-gradient(180deg,#9a9a9a,#555);border-radius:3px;opacity:.8}
.service h3{margin-top:21px;font-size:10px;font-weight:500;letter-spacing:1px;color:#444}
.service p{margin-top:18px;font-size:9.5px;font-weight:300;line-height:14px;color:var(--faint)}

/* footer */
.site-footer{position:absolute;left:0;top:976px;width:913px;height:165px;background:var(--footer);color:var(--footer-text)}
.col{position:absolute;top:24px;width:190px;font-size:9px;font-weight:300;line-height:15px}
.col h4{font-size:10px;font-weight:700;letter-spacing:1px;color:#fff;margin-bottom:15px}
.newsletter{display:flex;margin-top:15px}
.newsletter span{width:152px;height:33px;background:#fff;border-radius:2px 0 0 2px}
.newsletter b{width:37px;height:33px;background:var(--red);color:#fff;font-size:11px;font-weight:700;line-height:33px;text-align:center;border-radius:0 2px 2px 0}
.links li{list-style:none;margin-bottom:4px;font-size:8.5px}
.contact li{list-style:none;display:flex;gap:10px;margin-bottom:7px;line-height:14px}
.contact b{font-weight:500;color:#ccc}
.contact svg{flex:none;margin-top:3px}
.about hr{border:0;border-top:1px solid #777;margin:8px 0 14px}
.about .call-big{font-size:14px;color:#fff;font-weight:400;font-family:'Roboto',sans-serif}
.about .call-big span{color:var(--red);font-size:16px;font-weight:300}
.legal{position:absolute;left:0;top:1141px;width:913px;height:59px;background:var(--footer-deep)}
.legal p{position:absolute;left:45px;top:24px;font-size:9.5px;font-weight:300;color:#777}
.social{position:absolute;right:45px;top:24px;display:flex;gap:11px}
.social i{width:11px;height:11px;border-radius:50%;background:#777}
</style>
</head>
<body>

<header class="site-header">
  <div class="brand"><span class="brand-dot"></span>TowerLine</div>
  <div class="topbar">
    <span class="jobs">Employment Opportunities <b>Apply now!</b></span>
    <span class="call">
      <svg width="9" height="9" viewBox="0 0 24 24"><path fill="#e0201e" d="M6.6 10.8a15 15 0 006.6 6.6l2.2-2.2a1 1 0 011-.25 11.4 11.4 0 003.6.6 1 1 0 011 1V20a1 1 0 01-1 1A17 17 0 013 4a1 1 0 011-1h3.5a1 1 0 011 1c0 1.25.2 2.45.6 3.6a1 1 0 01-.25 1z"/></svg>
      CALL US: 555 014 2288
    </span>
    <div class="search">Start Typing...
      <svg width="13" height="13" viewBox="0 0 24 24"><circle cx="10" cy="10" r="7" fill="none" stroke="#999" stroke-width="3"/><path d="M15 15l6 6" stroke="#999" stroke-width="3"/></svg>
    </div>
  </div>
  <nav class="main-nav">
    <span>Home</span><span>About</span>
    <span>Monopole Reinforcements<span class="caret">&#8964;</span></span>
    <span>Tower Reinforcements<span class="caret">&#8964;</span></span>
    <span>Fabrication</span><span>Install</span><span>Contact</span>
  </nav>
</header>

<section class="hero" role="img" aria-label="Sunset over a forested horizon seen from high on a steel communication tower">
  <div class="hero-copy">
    <h1 class="hero-title">TOWERING <em>ABOVE</em> THE REST!</h1>
    <p class="hero-sub">REINFORCING FOR THE FUTURE</p>
    <span class="btn">READ MORE</span>
  </div>
</section>

<section class="overview">
  <h2 class="eyebrow">COMPANY OVERVIEW</h2>
  <div class="rule"></div>
  <p class="lead">TowerLine Inc. has expanded our product line to include specific<br>structural materials for your reinforcement requirements.</p>
  <span class="btn btn-about">LEARN MORE ABOUT US</span>
  <h2 class="services-title">Some of our core services</h2>

  <div class="service" style="left:34px">
    <div class="service-art" role="img" aria-label="Drawing of a reinforced monopole section"></div>
    <h3>MONOPOLE REINFORCEMENTS</h3>
    <p>Lorem ipsum dolor sit amet, consectetur adipiscing elit.<br>Nullam ornare sem sit amet mauris bibendum.</p>
  </div>
  <div class="service" style="left:316px">
    <div class="service-art" style="width:50px" role="img" aria-label="Drawing of a lattice tower section"></div>
    <h3>TOWER REINFORCEMENTS</h3>
    <p>Lorem ipsum dolor sit amet, consectetur adipiscing elit.<br>Nullam ornare sem sit amet mauris bibendum.</p>
  </div>
  <div class="service" style="left:597px">
    <div class="service-art" style="width:18px" role="img" aria-label="Drawing of a fabricated steel mast"></div>
    <h3>FABRICATION</h3>
    <p>Lorem ipsum dolor sit amet, consectetur adipiscing elit.<br>Nullam ornare sem sit amet mauris bibendum.</p>
  </div>
</section>

<footer class="site-footer">
  <div class="col" style="left:45px">
    <h4>STAY INFORMED</h4>
    <p>Enter your e-mail and subscribe to our<br>newsletter.</p>
    <div class="newsletter"><span></span><b>GO!</b></div>
  </div>
  <div class="col" style="left:256px">
    <h4>SERVICES</h4>
    <ul class="links">
      <li>MONOPOLE REINFORCEMENTS</li>
      <li>TOWER REINFORCEMENTS</li>
      <li>FABRICATION</li>
      <li>Install Services</li>
    </ul>
  </div>
  <div class="col" style="left:467px">
    <h4>CONTACT US</h4>
    <ul class="contact">
      <li><svg width="7" height="9" viewBox="0 0 24 30"><path fill="#999" d="M12 0a10 10 0 00-10 10c0 8 10 20 10 20s10-12 10-20A10 10 0 0012 0zm0 14a4 4 0 110-8 4 4 0 010 8z"/></svg><span><b>Address:</b> 1234 Street Name,<br>City Name, United States</span></li>
      <li><svg width="8" height="8" viewBox="0 0 24 24"><path fill="#999" d="M6.6 10.8a15 15 0 006.6 6.6l2.2-2.2a1 1 0 011-.25 11.4 11.4 0 003.6.6 1 1 0 011 1V20a1 1 0 01-1 1A17 17 0 013 4a1 1 0 011-1h3.5a1 1 0 011 1c0 1.25.2 2.45.6 3.6a1 1 0 01-.25 1z"/></svg><span><b>Phone:</b> (123) 456-7890</span></li>
      <li><svg width="9" height="7" viewBox="0 0 24 18"><path fill="#999" d="M0 0h24v18H0zM2 2l10 8 10-8z"/></svg><span><b>Email:</b> mail@example.com</span></li>
    </ul>
  </div>
  <div class="col about" style="left:678px">
    <h4>ABOUT US</h4>
    <p>Lorem ipsum dolor sit amet, consectetur<br>adipiscing elit. Donec eu pulvinar magna.</p>
    <hr>
    <p class="call-big">CALL US: <span>555 014 2288</span></p>
  </div>
</footer>

<div class="legal">
  <p>© 2014 TowerLine. All Rights Reserved.</p>
  <div class="social" aria-label="Social links"><i></i><i></i><i></i><i></i><i></i><i></i><i></i></div>
</div>

</body>
</html>
```